New label design for bakery products

We would like a new general label design for several bakery products (biscuits), made by producer "Pekarna Vrtovec".
We would like for the new packaging of the product to represent:
- Over 40 years of tradition
- No additives or preservatives
- Slovenian (local) ingredients
- Quality and homeliness of the product
- Hand crafted at certain stages of production
The label should be recktangular or oval. It should be colorful or brown. Logo should preferably stay the same - see the attached photo for reference (the man with a plate of cookies with text around it). Attached, you will also find a black and white logo of the company.
Here is the webpage of the company for more photo references: http://www.vrtovec-example.biz/index.html
The size of the label should be max. 12 x 7 cm.

```html
<!DOCTYPE html>
<html lang="sl">
<head>
<meta charset="utf-8">
<title>Orehove rezine – etiketa</title>
<link rel="stylesheet" href="https://fonts.googleapis.com/css2?family=Libre+Baskerville:wght@700&family=Arimo:wght@400;700&display=swap">
<style>
  :root {
    --page: #000000;
    --cream: #fdf5ea;
    --brown: #5a4b3f;
    --ink: #3f332b;
    --wheat: #efe4d4;
  }
  * { margin: 0; padding: 0; box-sizing: border-box; }
  html, body { width: 1200px; height: 1000px; overflow: hidden; background: var(--page); }
  .canvas { position: relative; width: 1200px; height: 1000px; }
  .label {
    position: absolute; left: 234px; top: 286px;
    width: 731px; height: 426px;
    background: var(--cream);
  }
  .brand-panel {
    position: absolute; left: 0; top: 0;
    width: 260px; height: 282px;
    background: var(--cream);
    text-align: center;
    color: var(--ink);
  }
  .brand-mark {
    position: absolute; left: 90px; top: 40px;
    width: 80px; height: 80px; border-radius: 50%;
    background: var(--brown);
  }
  .brand-name {
    position: absolute; left: 0; right: 0; top: 150px;
    font-family: "Libre Baskerville", Georgia, serif;
    font-weight: 700; font-size: 22px; line-height: 30px;
    color: var(--ink);
    letter-spacing: 0.5px;
  }
  .brand-contact {
    position: absolute; left: 0; right: 0; top: 230px;
    font-family: "Arimo", Arial, sans-serif;
    font-size: 14px; line-height: 20px; color: var(--ink);
  }
  .brand-footer {
    position: absolute; left: 0; top: 282px;
    width: 260px; height: 144px;
    background: var(--brown);
  }
  .product-header {
    position: absolute; left: 260px; top: 0;
    width: 471px; height: 92px;
    background: var(--brown);
    display: flex; align-items: center; justify-content: center;
  }
  .product-title {
    font-family: "Libre Baskerville", Georgia, serif;
    font-weight: 700; font-size: 35px; letter-spacing: 0.5px;
    color: var(--cream);
  }
  .ingredients {
    position: absolute; left: 301px; top: 106px;
    width: 388px;
    font-family: "Arimo", Arial, sans-serif;
    font-size: 10.6px; line-height: 15.2px;
    color: var(--ink);
    text-align: justify;
  }
  .ingredients strong { font-weight: 700; }
  .quality-badge {
    position: absolute; left: 301px; top: 352px;
    width: 56px; height: 56px;
    border: 2px solid var(--ink);
    background: var(--cream);
  }
  .quality-badge::after {
    content: ""; position: absolute; left: 0; right: 0; bottom: 0;
    height: 12px; background: var(--ink);
  }
  .best-before {
    position: absolute; left: 399px; top: 362px;
    font-family: "Arimo", Arial, sans-serif;
    font-weight: 700; font-size: 13.5px; line-height: 18px;
    color: var(--ink);
  }
</style>
</head>
<body>
<div class="canvas">
  <article class="label">
    <section class="brand-panel">
      <div class="brand-mark" aria-hidden="true"></div>
      <div class="brand-name">PEKARNA<br>VRTOVEC</div>
      <div class="brand-contact">LOGATEC, NOVA POT 14<br>TEL. 01/555 01 23</div>
    </section>
    <div class="brand-footer"></div>

    <header class="product-header">
      <h1 class="product-title">OREHOVE REZINE</h1>
    </header>

    <p class="ingredients">
      <strong>SESTAVINE:</strong> Psenicna bela moka, margarina: ( rastlinska olja ( palma ,oljna repica v spremenljivih delezih), voda, jedilna sol, emulgatorja : sojini lecitini, mono-in digleciridi mascobnih kislin, konzervansa: sorbiska kislina, citronska kislina, aroma, barvilo: <strong>SESTAVINE:</strong> Psenicna bela moka, margarina: ( rastlinska olja ( palma ,oljna repica v spremenljivih delezih), voda, jedilna sol, emulgatorja : sojini lecitini, mono-in digleciridi mascobnih kislin, konzervansa: sorbiska kislina, citronska kislina, aroma, barvilo: <strong>SESTAVINE:</strong> Psenicna bela moka, margarina: ( rastlinska olja ( palma ,oljna repica v spremenljivih delezih), voda, jedilna sol, emulgatorja : sojini lecitini, mono-in digleciridi mascobnih kislin, konzervansa: sorbiska kislina, citronska kislina <strong>SESTAVINE:</strong> Psenicna bela moka, margarina: ( rastlinska olja ( palma ,oljna repica v spremenljivih delezih), voda, jedilna sol.
    </p>

    <div class="quality-badge" role="img" aria-label="Znak kakovosti"></div>
    <p class="best-before">Uporabno<br>najmanj do :</p>
  </article>
</div>
</body>
</html>
```